Tri-fold Brochure Design for Banking Business

The brochure we have needs to be improved - more business like and more attractive. Logo file and brochure is attached. I would like to be able to edit the text after you get done. Your ideas and changes to text are welcome. See our website www.korvanbridgegrp.com for our theme. We can use indesign to edit the text after you complete. However, please make changes to the text we have in the design that it uploaded. Your comments and changes are welcome.

Target Market(s)

Human Resources and learning & development staff at the global investment banks - Pellham Trask, QWNR, etc.

Industry/Entity Type

Investment Banking

Logo Text

Korvan Bridge Group

Font styles to use
Serif
Sans Serif

Colors
33a6d7
0493ce
3277b5
fbf289
fdf9cf
fbee3e
0555a3
85acd3

Requirements
Must have
• Must be similar to our website www.korvanbridgegrp.com. Needs to be business-like, clean fonts, sharp design. Our logo - of course.
Nice to have
• City images - seems to be our theme.

```html
<!DOCTYPE html>
<html lang="en">
<head>
<meta charset="utf-8">
<title>Korvan Bridge Group – Tri-fold Brochure</title>
<link rel="stylesheet" href="https://fonts.googleapis.com/css2?family=Oswald:wght@300;400&family=PT+Sans:wght@400;700&display=swap">
<style>
  :root{
    --canvas:#d4d6d9;
    --navy:#0c3f6b;
    --deep:#0b5b93;
    --mid:#1679b8;
    --light:#2b9ad6;
    --sky:#85acd3;
    --pale:#eef3f8;
    --gold:#fbe33e;
    --ink:#10263d;
    --white:#ffffff;
  }
  *{margin:0;padding:0;box-sizing:border-box}
  html,body{width:785px;height:1200px;overflow:hidden;background:var(--canvas)}
  body{position:relative;font-family:"PT Sans",Arial,sans-serif;color:var(--white)}
  .spread{position:absolute;width:654px;height:508px;overflow:hidden;
    background:linear-gradient(90deg,var(--deep) 0%,var(--mid) 33%,var(--deep) 34%,var(--mid) 66%,var(--deep) 67%,var(--mid) 100%);
    box-shadow:0 10px 10px -6px rgba(0,0,0,.35)}
  .spread--outside{left:57px;top:56px}
  .spread--inside{left:59px;top:623px}
  .fold{position:absolute;top:0;width:1px;height:100%;background:rgba(0,0,0,.12)}
  .photo{position:absolute;inset:0}
  .strip{position:absolute;inset:0;background:rgba(255,255,255,.55)}
  .abs{position:absolute}
  .heading{font-family:"Oswald",Arial,sans-serif;font-weight:300;font-size:14.5px;letter-spacing:-.2px;text-transform:uppercase;line-height:1}
  .rule{height:1px;background:var(--gold);margin-top:6px;width:78px}
  .body-text{font-size:7.6px;line-height:1.38;text-align:justify}
  .body-text p{margin-bottom:8px}
  .url{font-size:10px;color:var(--gold)}
  .logo{display:flex;align-items:center;gap:6px;font-family:"Oswald",Arial,sans-serif;font-weight:400;font-size:16px;letter-spacing:1px;color:var(--ink)}
  .logo-mark{width:14px;height:14px;background:var(--ink)}
  .contact{font-size:7px;line-height:1.5}
  .list{list-style:none;font-size:7.6px;line-height:1.3}
  .list li{position:relative;padding-left:16px;margin-bottom:8px;text-align:justify}
  .list--boxes li::before{content:"";position:absolute;left:0;top:1px;width:7px;height:7px;border:1.2px solid var(--white)}
  .list--dots li{margin-bottom:7px;text-align:left}
  .list--dots li::before{content:"";position:absolute;left:0;top:1px;width:7px;height:7px;border-radius:50%;background:var(--gold)}
</style>
</head>
<body>

<!-- Outside of the brochure -->
<section class="spread spread--outside">
  <div class="photo" role="img" aria-label="Businessman touching a virtual training interface"
       style="clip-path:polygon(0 0,218px 0,218px 250px,0 205px);background:linear-gradient(135deg,#b9d6ee 0%,#5b98c8 45%,#1d5f97 100%)"></div>
  <div class="strip" style="clip-path:polygon(0 205px,218px 250px,218px 262px,0 222px)"></div>

  <div class="photo" role="img" aria-label="City skyline with world map and network lines"
       style="clip-path:polygon(218px 0,436px 0,436px 299px,326px 319px,218px 266px);background:linear-gradient(180deg,#f4f8fb 0%,#c8dcec 45%,#7fa9cc 100%)"></div>

  <div class="photo" role="img" aria-label="Businessman looking over a sunlit city"
       style="clip-path:polygon(436px 0,654px 0,654px 339px,436px 299px);background:linear-gradient(180deg,#eef3f8 0%,#d9e2ec 50%,#f4dcc6 100%)"></div>
  <div class="strip" style="clip-path:polygon(436px 299px,654px 339px,654px 350px,436px 312px)"></div>

  <div class="fold" style="left:218px"></div>
  <div class="fold" style="left:436px"></div>

  <!-- Back cover -->
  <div class="abs" style="left:64px;top:76px;font-family:'Oswald',sans-serif;font-size:27px;font-weight:400">TRAINING</div>
  <div class="abs" style="left:11px;top:108px;font-family:'Oswald',sans-serif;font-size:10px;font-weight:300;word-spacing:5px;white-space:nowrap">MENTOR MOTIVATION SKILL KNOWLEDGE</div>

  <div class="abs" style="left:15px;top:269px;width:190px">
    <h2 class="heading">About Us</h2>
    <div class="rule"></div>
    <div class="body-text" style="margin-top:10px">
      <p>Korvan Bridge Group's dedicated staff is able to efficiently provide complete sales, marketing and logistical support for all our programs, no matter the location.</p>
      <p>Our globally located trainers have extensive experience, both as industry professionals and as trainers.</p>
      <p>Their efforts are complemented by our highly trained logistical support team supported by the latest Lumen Office Hub, Korvan and customer management systems.</p>
    </div>
  </div>
  <div class="abs url" style="left:42px;top:472px">www.korvanbridgegrp.com</div>

  <!-- Inner flap -->
  <div class="abs" style="left:252px;top:50px">
    <div class="logo"><span class="logo-mark"></span>KORVAN BRIDGE GROUP</div>
  </div>
  <div class="abs" style="left:246px;top:88px;font-family:'Oswald',sans-serif;font-size:13px;font-weight:400;color:var(--ink)">WORLDWIDE TRAINING SERVICE</div>

  <div class="abs" style="left:245px;top:374px;width:180px">
    <h2 class="heading">Get In Touch</h2>
    <div class="rule"></div>
    <div class="contact" style="margin-top:7px">
      GLOBAL:<br>nadia.ferro@korvanbridgegrp.com<br>
      ASIA:<br>owen.castell@korvanbridgegrp.com<br>
      UNITED STATES:<br>leo.marsh@korvanbridgegrp.com<br>
      EUROPE:<br>tomas.lind@korvanbridgegrp.com
    </div>
  </div>

  <!-- Front cover -->
  <div class="abs" style="left:466px;top:40px">
    <div class="logo"><span class="logo-mark"></span>KORVAN BRIDGE GROUP</div>
  </div>
  <div class="abs" style="left:449px;top:404px;font-family:'Oswald',sans-serif;font-weight:300;font-size:19px;line-height:1.4;color:var(--gold)">YOUR EXPERT TRAINING AND<br>CONSULTING PARTNER</div>
  <div class="abs url" style="left:449px;top:472px">www.korvanbridgegrp.com</div>
</section>

<!-- Inside of the brochure -->
<section class="spread spread--inside">
  <div class="photo" role="img" aria-label="Businessman with tablet blended with city towers"
       style="clip-path:polygon(0 0,218px 0,218px 253px,0 212px);background:linear-gradient(180deg,#f7f9fb 0%,#c5d4e2 45%,#6f8aa4 100%)"></div>
  <div class="strip" style="clip-path:polygon(0 212px,218px 253px,218px 265px,0 228px)"></div>

  <div class="photo" role="img" aria-label="Soft-focus city skyline"
       style="clip-path:polygon(218px 0,436px 0,436px 215px,218px 260px);background:linear-gradient(180deg,#f5f8fb 0%,#dbe7f1 55%,#a9c4da 100%)"></div>
  <div class="strip" style="clip-path:polygon(218px 260px,436px 215px,436px 226px,218px 272px)"></div>

  <div class="photo" role="img" aria-label="Hands working on a tablet at a meeting table"
       style="clip-path:polygon(436px 293px,654px 245px,654px 508px,436px 508px);background:linear-gradient(160deg,#e9eef3 0%,#b7c4d0 55%,#7a8a99 100%)"></div>
  <div class="strip" style="clip-path:polygon(436px 281px,654px 233px,654px 245px,436px 293px)"></div>

  <div class="fold" style="left:218px"></div>
  <div class="fold" style="left:436px"></div>

  <div class="abs" style="left:15px;top:272px;width:190px">
    <h2 class="heading">Our Services</h2>
    <div class="rule"></div>
    <ul class="list list--boxes" style="margin-top:12px">
      <li>Korvan Bridge Group provides best in class services for all our clients.</li>
      <li>We provide highly customized programs tailored to your specific requirements.</li>
      <li>Direct interaction between our clients, consulting trainers and client service staff ensures measurable outcomes for program participants.</li>
      <li>We facilitate learning outcomes using a blended methodology combining interactive analysis, hands-on experiential models, market simulations and a state-of-the-art learning management system.</li>
      <li>Our material databanks are continuously updated to insure accuracy and effectiveness of our services.</li>
    </ul>
  </div>

  <div class="abs" style="left:237px;top:272px;width:192px">
    <h2 class="heading">Why Choose Us?</h2>
    <div class="rule"></div>
    <div class="body-text" style="margin-top:12px">
      <p>Korvan Bridge Group provides expert in-house training for your staff. We cover a wide range of topic areas and can readily provide customized content to match your requirements.</p>
    </div>
    <ul class="list list--dots">
      <li>Highly qualified, international pool of trainers</li>
      <li>Strong client relationship management and support</li>
      <li>Competitive pricing and flexibility</li>
      <li>Outcome driven approach directly matches your company's needs</li>
    </ul>
    <div class="body-text" style="margin-top:4px">
      <p>Our Consulting Trainers are sourced globally and recognized by the industry as highly effective trainers and program facilitators.</p>
    </div>
  </div>

  <div class="abs" style="left:454px;top:31px;width:182px">
    <h2 class="heading">Our Team</h2>
    <div class="rule"></div>
    <div class="body-text" style="margin-top:10px;text-align:left">
      <p>Our Consulting Trainers are located globally and recognized by the industry as highly effective trainers and program facilitators.</p>
      <p>Korvan provides global expertise for our programs with local talent for program facilitation.</p>
      <p>Our large array of Consulting Trainers lets Korvan provide global expertise for our programs while using local talent for program facilitation.</p>
    </div>
  </div>
  <div class="abs url" style="left:454px;top:201px">www.korvanbridgegrp.com</div>
</section>

</body>
</html>
```